Flyer-Design für ein Cheerleader Team
Zielgruppe
Hallo, wir sind ein Cheerleader Team, wir suchen Kinder von 5-11 Jugendliche von 11-16 und junge Erwachsene ab 16
Wir suchen sportbegeisterte Kinder/Leute die Spaß haben neues zu lernen und viel Abwechslung brauchen/möchten.
Wir bieten ausgebildete Trainer 4 Wochen Probezeit kostenfrei.
Unser Sport beinhaltet
Akrobatik , Stunts, Tanz, turnen und Sprünge.
Unsere Teamfarben sind blau, Silber, weiß und schwarz ist auch ok
Die Farben sollten auch verwendet werden.
Aufgabenstellung
Infos:
Falken Cheerleader Hamburg
Verein SpVg Lindenau- Brockhorst
4 Wochen gratis Probetraining!
Anfänger erwünscht
Ein TeamSport aus Stunts, Akrobatik, Tanz und Turnen

```html
<!DOCTYPE html>
<html lang="de">
<head>
<meta charset="utf-8">
<title>Falken Cheerleader Hamburg – Flyer</title>
<link rel="stylesheet" href="https://fonts.googleapis.com/css2?family=Archivo:wght@400;500;800;900&display=swap">
<style>
  :root {
    --navy: #1b1f5c;
    --navy-deep: #0c0f3d;
    --sky: #4aa3dc;
    --sky-text: #3c9bd6;
    --paper: #f4f4f4;
    --ink: #2a2a3a;
    --stage: #d3d3d3;
  }
  * { margin: 0; padding: 0; box-sizing: border-box; }
  html, body { width: 1200px; height: 960px; overflow: hidden; }
  body {
    background: var(--stage);
    font-family: "Archivo", sans-serif;
    display: flex; align-items: center; justify-content: center;
  }
  .flyer {
    position: relative;
    width: 640px; height: 905px;
    background: var(--paper);
    overflow: hidden;
  }
  .navy-block {
    position: absolute; left: 0; top: 0;
    width: 378px; height: 443px;
    background: linear-gradient(160deg, var(--navy) 0%, var(--navy-deep) 55%, var(--navy) 100%);
  }
  .club-name {
    position: absolute; left: 396px; top: 36px;
    display: flex; align-items: center; gap: 8px;
    color: var(--navy-deep);
    font-weight: 800; font-size: 15px; line-height: 1.05; letter-spacing: .04em;
    text-transform: uppercase;
  }
  .club-name .dot {
    width: 24px; height: 24px; border-radius: 50%; background: var(--navy);
  }
  .photo {
    position: absolute; left: 122px; top: 108px;
    width: 420px; height: 560px;
    background: linear-gradient(180deg, #b9cde0 0%, #d9dccf 28%, #e6d7a8 38%, #5b6b4a 46%, #2b3266 60%, #a8a39c 82%, #8f8b86 100%);
  }
  .association {
    position: absolute; left: 592px; top: 355px;
    transform-origin: left top; transform: rotate(-90deg);
    white-space: nowrap;
    font-size: 13px; font-weight: 500; letter-spacing: .09em;
    color: var(--ink); text-transform: uppercase;
  }
  .headline {
    position: absolute; left: 70px; top: 418px;
    font-weight: 900; font-size: 60px; line-height: 1; text-transform: uppercase;
    color: var(--sky-text); letter-spacing: -.01em;
  }
  .headline span {
    display: block; width: max-content;
    background: rgba(244,244,244,.88);
    padding: 3px 10px 2px;
    margin-bottom: 6px;
  }
  .headline .line-2 { margin-left: 26px; }
  .headline .line-3 { margin-left: 52px; }
  .offer-band {
    position: absolute; left: 360px; top: 574px;
    width: 280px; height: 70px;
    background: var(--sky);
    display: flex; align-items: center; gap: 10px;
    padding-left: 16px;
    color: var(--navy);
  }
  .offer-band .number { font-weight: 900; font-size: 52px; line-height: 1; }
  .offer-band .label {
    font-weight: 500; font-size: 17px; line-height: 1.1; text-transform: uppercase; letter-spacing: .02em;
  }
  .copy {
    position: absolute;
    font-size: 11px; line-height: 1.4; color: var(--ink);
  }
  .copy-offer { left: 410px; top: 690px; width: 200px; }
  .copy-audience { left: 130px; top: 770px; width: 250px; }
</style>
</head>
<body>
  <main class="flyer">
    <div class="navy-block"></div>
    <div class="club-name"><span class="dot"></span><span>Falken<br>Cheerleader</span></div>
    <div class="photo" role="img" aria-label="Foto: Cheerleaderinnen in blauen Uniformen heben eine Flyerin bei Sonnenuntergang am See in die Luft"></div>
    <p class="association">Verein SpVg Lindenau-Brockhorst</p>
    <h1 class="headline">
      <span class="line-1">Cheer</span>
      <span class="line-2">Leader</span>
      <span class="line-3">Team</span>
    </h1>
    <div class="offer-band">
      <span class="number">4</span>
      <span class="label">Wochen kostenloses<br>Probetraining</span>
    </div>
    <p class="copy copy-offer">Wir bieten ausgebildete Trainer und eine kostenfreie Probezeit von vier Wochen. Unser Sport beinhaltet Akrobatik, Stunts, Tanz, Turnen und Sprünge.</p>
    <p class="copy copy-audience">Wir suchen sportbegeisterte Kinder 5-11 Jahre, Jugendliche 11-16 und junge Erwachsene ab 16 Jahren, die Spaß haben Neues zu lernen.</p>
  </main>
</body>
</html>
```